" Empresa jovem, em franca expansao, com necessidade de ampliar e qualificar sua carteira de clientes, buscando aprimorar sua identidade visual para se destacar em uma concorrência com pouco investimento nesse fundamento corporativo e potencializar sua apresentaçao a clientes de grande porte. "

```html
<!DOCTYPE html>
<html lang="pt-BR">
<head>
<meta charset="utf-8">
<title>Assinatura de e-mail – Afiadora Serrana</title>
<link href="https://fonts.googleapis.com/css2?family=Open+Sans:wght@400;600&display=swap" rel="stylesheet">
<style>
  :root {
    --backdrop: #a8683a;
    --navy: #1d3a5f;
    --panel-light: #f2f3f4;
    --panel-shade: #dfe1e3;
    --white: #ffffff;
    --muted: #c9d3df;
  }
  * { margin: 0; padding: 0; box-sizing: border-box; }
  html, body {
    width: 1200px; height: 1200px; overflow: hidden;
    background: var(--backdrop);
    font-family: "Open Sans", Arial, sans-serif;
  }
  .signature {
    position: absolute; left: 132px; top: 509px;
    width: 936px; height: 254px;
    display: flex;
    box-shadow: 0 6px 14px rgba(0,0,0,0.25);
    border-top-right-radius: 62px;
  }
  .brand-panel {
    width: 547px; height: 100%;
    background: linear-gradient(115deg, var(--panel-light) 0%, var(--white) 40%, var(--panel-shade) 100%);
    display: flex; flex-direction: column; align-items: center; justify-content: center;
    gap: 18px;
  }
  .brand-mark {
    width: 78px; height: 78px; background: var(--navy);
  }
  .brand-name {
    color: var(--navy); font-weight: 600; font-size: 40px;
    letter-spacing: 2px; text-transform: uppercase; line-height: 1;
  }
  .contact-panel {
    flex: 1; height: 100%;
    background: var(--navy);
    border-top-right-radius: 62px;
    color: var(--white);
    padding: 34px 0 0 19px;
  }
  .person-name { font-size: 25px; font-weight: 400; line-height: 1.1; }
  .person-role { font-size: 15px; color: var(--muted); margin-top: 2px; }
  .contact-list { list-style: none; margin-top: 22px; }
  .contact-item {
    display: flex; align-items: flex-start;
    font-size: 18px; line-height: 22px; margin-bottom: 9px;
  }
  .contact-icon { width: 20px; height: 20px; margin: 1px 18px 0 0; flex: none; }
</style>
</head>
<body>
  <section class="signature">
    <div class="brand-panel">
      <div class="brand-mark"></div>
      <div class="brand-name">Afiadora Serrana</div>
    </div>
    <div class="contact-panel">
      <p class="person-name">Paulo Henrique</p>
      <p class="person-role">Diretor</p>
      <ul class="contact-list">
        <li class="contact-item">
          <svg class="contact-icon" viewBox="0 0 20 20"><rect x="2" y="5" width="16" height="11" fill="#fff"/><path d="M2 5 L10 11 L18 5" stroke="#1d3a5f" stroke-width="1.5" fill="none"/></svg>
          <span>Rua das Acácias, 210 Centro<br>Vale Alto&nbsp; MG</span>
        </li>
        <li class="contact-item">
          <svg class="contact-icon" viewBox="0 0 20 20"><path d="M5 2 L8 2 L9 6 L7 8 Q9 12 12 13 L14 11 L18 12 L18 15 Q17 18 14 17 Q4 14 3 5 Q3 2 5 2 Z" fill="#fff"/></svg>
          <span>34 5555-0101</span>
        </li>
        <li class="contact-item">
          <svg class="contact-icon" viewBox="0 0 20 20"><text x="10" y="16" text-anchor="middle" font-family="Open Sans, sans-serif" font-size="17" font-weight="600" fill="#fff">@</text></svg>
          <span>contato@serrana.com.br</span>
        </li>
        <li class="contact-item">
          <svg class="contact-icon" viewBox="0 0 20 20"><circle cx="10" cy="10" r="7.5" stroke="#fff" stroke-width="1.6" fill="none"/><path d="M2.5 10 H17.5 M10 2.5 Q5 10 10 17.5 M10 2.5 Q15 10 10 17.5" stroke="#fff" stroke-width="1.3" fill="none"/></svg>
          <span>www.serrana.com.br</span>
        </li>
      </ul>
    </div>
  </section>
</body>
</html>
```